Kestrel Forge Tech
Bus. Cards/Stationary/Presentation
Kestrel Forge Tech - Information Technology
Creative Brief
Use specific fonts
Open to ideas on font pairing
Professional
Wendell Pask
Owner
218 Larkspur Avenue Suite 4400 Alder Bend, OR 97321
Wendell.Pask@kestrelforgetech.com
www.kestrelforgetech.com
I am open to my logo displayed on the back. I am also open to ideas on the back of business card. Be creative on front and back.

```html
<!DOCTYPE html>
<html lang="en">
<head>
<meta charset="UTF-8">
<title>Kestrel Forge Tech – Business Cards</title>
<link href="https://fonts.googleapis.com/css2?family=Open+Sans:wght@400;600;700&display=swap" rel="stylesheet">
<style>
  :root {
    --stage: #2e2e2e;
    --paper: #ffffff;
    --ink: #6b6b6b;
    --ink-dark: #4a4a4a;
    --green: #6cc04a;
    --green-deep: #2f9a3a;
    --grey-card: #6f6f6f;
    --grey-card-dark: #555555;
    --swoosh-light: #e4e4e4;
    --band: #707070;
  }
  * { margin: 0; padding: 0; box-sizing: border-box; }
  html, body {
    width: 1200px; height: 792px; overflow: hidden;
    background: var(--stage);
    font-family: "Open Sans", Arial, sans-serif;
  }
  .sheet {
    position: relative; width: 1200px; height: 792px;
    display: grid;
    grid-template-columns: 530px 530px;
    grid-template-rows: 330px 330px;
    gap: 32px 40px;
    padding: 50px 50px;
  }
  .card {
    position: relative; overflow: hidden;
    border-radius: 14px;
    box-shadow: 0 6px 18px rgba(0,0,0,0.45);
  }
  .card--front, .card--logo { background: var(--paper); }
  .card--grey { background: radial-gradient(circle at 50% 45%, var(--grey-card), var(--grey-card-dark)); }
  .card--green { background: radial-gradient(circle at 50% 45%, var(--green), var(--green-deep)); }

  .brand { display: flex; flex-direction: column; align-items: center; gap: 12px; }
  .brand__dot { width: 34px; height: 34px; border-radius: 50%; background: var(--green); flex: none; }
  .brand__name { font-weight: 700; color: var(--ink-dark); white-space: nowrap; }

  /* front card */
  .front__brand { position: absolute; left: 20px; top: 62px; width: 236px; }
  .front__brand .brand__name { font-size: 22px; }
  .front__divider { position: absolute; left: 262px; top: 42px; width: 2px; height: 138px; background: var(--green); }
  .front__contact { position: absolute; left: 280px; top: 42px; color: var(--ink); font-size: 11px; line-height: 1.5; }
  .contact__name { color: var(--green); font-size: 17px; font-weight: 600; line-height: 1.2; }
  .contact__role { font-size: 12px; margin-bottom: 12px; }
  .contact__address { margin-bottom: 10px; }
  .contact__label { color: var(--green); font-weight: 700; display: inline-block; width: 12px; }
  .front__wave { position: absolute; left: 0; bottom: 0; width: 530px; height: 330px; }
  .front__web { position: absolute; right: 26px; bottom: 18px; color: #fff; font-size: 15px; font-weight: 600; letter-spacing: 1px; }

  /* logo side */
  .logo__brand { position: absolute; left: 0; right: 0; top: 112px; }
  .logo__brand .brand { flex-direction: row; justify-content: center; }
  .logo__brand .brand__name { font-size: 32px; }
  .logo__web { position: absolute; left: 0; right: 0; bottom: 70px; text-align: center; color: var(--ink); font-size: 13px; letter-spacing: 2px; font-weight: 600; }

  /* back sides */
  .back__brand { position: absolute; left: 0; right: 0; top: 100px; }
  .back__brand .brand__dot { width: 48px; height: 48px; background: #fff; }
  .back__brand .brand__name { font-size: 34px; color: #fff; }
  .back__web { position: absolute; left: 0; right: 0; bottom: 34px; text-align: center; color: #fff; font-size: 13px; letter-spacing: 2px; font-weight: 600; }
</style>
</head>
<body>
<main class="sheet">

  <section class="card card--front">
    <svg class="front__wave" viewBox="0 0 530 330" aria-hidden="true">
      <path d="M0 205 C140 250 330 250 530 190 L530 330 L0 330 Z" fill="var(--swoosh-light)"/>
      <path d="M0 245 C170 272 360 255 530 200 L530 222 C360 272 170 290 0 268 Z" fill="var(--green)"/>
      <path d="M0 282 C200 292 390 272 530 236 L530 330 L0 330 Z" fill="var(--band)"/>
    </svg>
    <div class="front__brand brand">
      <span class="brand__dot"></span>
      <span class="brand__name">Kestrel Forge Tech</span>
    </div>
    <div class="front__divider"></div>
    <div class="front__contact">
      <div class="contact__name">Wendell Pask</div>
      <div class="contact__role">Owner</div>
      <div class="contact__address">218 Larkspur Avenue, Suite 4400<br>Alder Bend, OR 97321</div>
      <div><span class="contact__label">P</span>: 541.555.0147</div>
      <div><span class="contact__label">C</span>: 541.555.0183</div>
      <div><span class="contact__label">F</span>: 541.555.0162</div>
      <div><span class="contact__label">E</span>: Wendell.Pask@kestrelforgetech.com</div>
    </div>
    <div class="front__web">www.kestrelforgetech.com</div>
  </section>

  <section class="card card--logo">
    <div class="logo__brand">
      <div class="brand">
        <span class="brand__dot"></span>
        <span class="brand__name">Kestrel Forge Tech</span>
      </div>
    </div>
    <div class="logo__web">www.kestrelforgetech.com</div>
  </section>

  <section class="card card--grey">
    <div class="back__brand brand">
      <span class="brand__dot"></span>
      <span class="brand__name">Kestrel Forge Tech</span>
    </div>
    <div class="back__web">www.kestrelforgetech.com</div>
  </section>

  <section class="card card--green">
    <div class="back__brand brand">
      <span class="brand__dot"></span>
      <span class="brand__name">Kestrel Forge Tech</span>
    </div>
    <div class="back__web">www.kestrelforgetech.com</div>
  </section>

</main>
</body>
</html>
```